Velmora and Quorvista Ad Designs

I am looking for a set of 3 Velmora and 2 Quorvista Ads designed to entice men aged 20 to 40 to download a free report which teaches them about the causes of hair loss and the available treatment options. The ads in the set can be a variation on the same theme or they can be completely different.

I have attached a copy of the report for reference.

Velmora Ad Size Specifications:
Size: 1,200 x 628 pixels.
Image ratio: 1.9:1.
No more than 20% of the image area should be covered by text.
Note that there does not need to be any text if an image will work as we do have the text that goes with the ad to use.
Check the amount of text in the image here: https://www.velmora-ads.example/ads/tools/text_overlay

Quorvista Ad Size Specifications:
Size: 1080 x 1080 pixels
Image format: .jpg or .png
Max. file size: 30 MB

Target Market(s)

Males between 20 to 40 years old who have hair that is starting to thin or recede and want to know about why this is happening and what options they have for treatment.

Industry/Entity Type

Health And Wellness

Font styles to use
Serif
Sans Serif

Colors

Designer to choose colors to be used in the design.

Requirements
Must have
• Positive eye catching imagery.
• VM does not allow ads that make people feel bad, so the image must be positive and happy.
Nice to have
• Faces looking directly at the user seem to work well but open to anything that will catch people's attention and get them to download.
Should not have
• Must not include any branding. The report is independent.
• Must not have sad or unhappy looking people in the report.

```html
<!DOCTYPE html>
<html lang="en">
<head>
<meta charset="utf-8">
<title>The Best Hair Loss Treatments – Free Report Ad</title>
<link rel="stylesheet" href="https://fonts.googleapis.com/css2?family=Roboto+Condensed:wght@300;400;700&family=Roboto:wght@300;400;700&display=swap">
<style>
  :root {
    --teal-light: #7fb4ae;
    --teal-text: #4b8e88;
    --navy: #0f5a7d;
    --gold: #e4b10f;
    --ink: #222a2e;
    --white: #ffffff;
    --device: #111314;
    --sky-top: #c7e3ee;
    --sky-mid: #9fcbdc;
    --sea: #8fb6c2;
    --sand: #b89d7c;
  }
  * { margin: 0; padding: 0; box-sizing: border-box; }
  html, body { width: 1200px; height: 628px; overflow: hidden; background: #fff; }
  .ad {
    position: relative;
    width: 1200px;
    height: 628px;
    overflow: hidden;
    font-family: "Roboto Condensed", "Roboto", sans-serif;
  }
  .scene-photo {
    position: absolute; inset: 0;
    background: linear-gradient(180deg, var(--sky-top) 0%, var(--sky-mid) 35%, var(--sea) 45%, #c9bba6 62%, var(--sand) 100%);
  }
  .scene-fade {
    position: absolute; left: 0; top: 0; width: 520px; height: 628px;
    background: linear-gradient(90deg, rgba(255,255,255,0.75) 0%, rgba(255,255,255,0.35) 60%, rgba(255,255,255,0) 100%);
  }
  .accent-bands { position: absolute; inset: 0; }
  .badge {
    position: absolute; left: 942px; top: 36px; width: 258px; height: 48px;
    background: var(--gold); color: var(--white);
    font-family: "Roboto", sans-serif; font-weight: 700; font-size: 19px;
    letter-spacing: 1px; display: flex; align-items: center; justify-content: center;
  }
  .headline { position: absolute; left: 26px; top: 252px; text-transform: uppercase; }
  .headline__lead { display: block; font-weight: 300; font-size: 54px; line-height: 56px; color: var(--ink); }
  .headline__main { display: block; font-weight: 700; font-size: 66px; line-height: 64px; color: var(--teal-text); }
  .tablet {
    position: absolute; left: 793px; top: 185px; width: 280px; height: 398px;
    background: var(--device); border-radius: 22px;
  }
  .tablet__camera { position: absolute; left: 136px; top: 14px; width: 7px; height: 7px; border-radius: 50%; background: #333; }
  .tablet__button { position: absolute; left: 128px; top: 372px; width: 22px; height: 22px; border-radius: 50%; border: 2px solid #333; }
  .cover {
    position: absolute; left: 17px; top: 37px; width: 246px; height: 328px;
    background: var(--white); overflow: hidden;
  }
  .cover__portrait {
    position: absolute; left: 0; top: 82px; width: 246px; height: 196px;
    background: linear-gradient(135deg, #d9d9d9 0%, #8c8c8c 45%, #3d3d3d 100%);
  }
  .cover__bands { position: absolute; inset: 0; }
  .cover__kicker { position: absolute; left: 8px; top: 56px; font-weight: 300; font-size: 24px; line-height: 24px; color: var(--gold); }
  .cover__title {
    position: absolute; left: 6px; top: 80px; padding: 1px 4px;
    background: var(--navy); color: var(--white); font-weight: 700; font-size: 18px; line-height: 20px;
  }
  .cover__year { position: absolute; right: 8px; top: 202px; text-align: right; }
  .cover__year-num { display: block; font-weight: 700; font-size: 34px; line-height: 32px; color: var(--white); }
  .cover__year-label { display: block; font-weight: 400; font-size: 22px; line-height: 22px; color: var(--gold); }
  .cover__footer { position: absolute; left: 8px; bottom: 8px; color: var(--white); text-transform: uppercase; }
  .cover__footer-top { display: block; font-size: 11px; line-height: 13px; font-weight: 400; }
  .cover__footer-main { display: block; font-size: 14px; line-height: 16px; font-weight: 400; }
  .cover__byline { display: block; font-size: 5px; line-height: 8px; font-weight: 400; }
</style>
</head>
<body>
<main class="ad">
  <div class="scene-photo" role="img" aria-label="Photo of a smiling, confident young man with full curly hair and sunglasses, hand in his hair, standing on a sunny beach pier by the sea"></div>
  <div class="scene-fade"></div>

  <svg class="accent-bands" width="1200" height="628" viewBox="0 0 1200 628" aria-hidden="true">
    <polygon points="0,0 530,0 0,118" fill="var(--teal-light)"/>
    <polygon points="0,132 560,0 650,0 0,152" fill="var(--gold)"/>
    <polygon points="0,152 300,72 0,196" fill="var(--navy)"/>
    <polygon points="640,628 1200,410 1200,440 705,628" fill="var(--gold)"/>
    <polygon points="760,628 1200,468 1200,628" fill="var(--navy)"/>
  </svg>

  <div class="badge">FREE REPORT</div>

  <h1 class="headline">
    <span class="headline__lead">The Best</span>
    <span class="headline__main">Hair Loss</span>
    <span class="headline__main">Treatments</span>
  </h1>

  <div class="tablet">
    <span class="tablet__camera"></span>
    <div class="cover">
      <div class="cover__portrait" role="img" aria-label="Black and white portrait photo of a young man for the report cover"></div>
      <svg class="cover__bands" width="246" height="328" viewBox="0 0 246 328" aria-hidden="true">
        <polygon points="0,0 246,0 246,6 0,38" fill="var(--navy)"/>
        <polygon points="0,0 130,0 0,18" fill="var(--teal-light)"/>
        <polygon points="150,12 246,0 246,30" fill="var(--gold)"/>
        <polygon points="0,38 246,6 246,12 0,44" fill="var(--gold)"/>
        <polygon points="0,292 246,258 246,266 0,300" fill="var(--gold)"/>
        <polygon points="0,300 246,266 246,328 0,328" fill="var(--navy)"/>
      </svg>
      <div class="cover__kicker">BEST OF</div>
      <div class="cover__title">HAIR LOSS TREATMENTS</div>
      <div class="cover__year">
        <span class="cover__year-num">2018</span>
        <span class="cover__year-label">REVIEW</span>
      </div>
      <div class="cover__footer">
        <span class="cover__footer-top">Independent guide to</span>
        <span class="cover__footer-main">Hair growth products</span>
        <span class="cover__byline">By Cal Ransome - Youthful aging, wellness &amp; lifestyle expert</span>
      </div>
    </div>
    <span class="tablet__button"></span>
  </div>
</main>
</body>
</html>
```